Outpatient imaging center needs a flyer design

Flyer must include the provided logo.
Orange/Yellow color is being included
MRI scanner image-
A4, Z fold, 6 pages-double sized

healthcare

F0912C
F2A743
F7CA91
FBE8D2
FDF5EE

```html
<!DOCTYPE html>
<html lang="en">
<head>
<meta charset="utf-8">
<title>Clearview MRI – Imaging Flyer</title>
<link href="https://fonts.googleapis.com/css2?family=Roboto:wght@300;400;500;700&display=swap" rel="stylesheet">
<style>
  :root{
    --orange:#F0912C;
    --amber:#F2A743;
    --peach:#F7CA91;
    --cream:#FBE8D2;
    --ivory:#FDF5EE;
    --grey:#8f8f92;
    --grey-ring:#9b9b9e;
    --grey-soft:#ececec;
    --ink:#1e1e1e;
    --text:#444;
    --white:#ffffff;
    --backdrop:#efece8;
  }
  *{margin:0;padding:0;box-sizing:border-box}
  html,body{width:1200px;height:873px;overflow:hidden}
  body{background:var(--backdrop);font-family:'Roboto',sans-serif;position:relative}
  .page{position:absolute;top:70px;width:471px;height:665px;background:var(--white);overflow:hidden;box-shadow:0 4px 14px rgba(0,0,0,.12)}
  .page--front{left:94px}
  .page--back{left:620px}
  .page__shapes{position:absolute;inset:0}
  .abs{position:absolute}

  /* front page */
  .brand{left:33px;top:40px;display:flex;align-items:center;gap:6px;font-size:19px;font-weight:500;color:var(--grey);letter-spacing:.5px}
  .brand__dot{width:14px;height:14px;border-radius:50%;background:var(--orange)}
  .scanner-photo{left:280px;top:12px;width:190px;height:166px;border-radius:8px;background:linear-gradient(160deg,#f1f2f4,#d6d9de 60%,#c4c8cf)}
  .exam-photo{left:37px;top:104px;width:130px;height:130px;border-radius:50%;background:linear-gradient(160deg,#e9ecf0,#c9cfd8 55%,#8fa6cf 80%,#dfe3ea);box-shadow:0 0 0 5px var(--white)}
  .intro{left:126px;top:248px;width:223px;color:var(--white);text-align:center}
  .intro__title{font-size:15px;font-weight:400;letter-spacing:.3px;padding-bottom:9px;border-bottom:2px solid var(--white);margin-bottom:7px}
  .intro__text{font-size:9.6px;font-weight:300;line-height:13.3px;text-align:justify;text-align-last:center}
  .service{top:457px;width:200px}
  .service--cardiac{left:21px}
  .service--body{left:251px}
  .service__title{font-size:15.5px;font-weight:700;color:var(--orange);margin-bottom:10px;white-space:nowrap}
  .service__text{font-size:8.6px;line-height:13.3px;color:#666;text-align:justify}
  .service__price{position:absolute;top:126px;font-size:15.5px;font-weight:700;color:var(--orange);white-space:nowrap}

  /* back page */
  .why{left:0;top:16px;width:471px;text-align:center}
  .why__title{font-size:23px;font-weight:700;color:var(--ink);margin-bottom:6px}
  .why__lead{font-size:9.4px;line-height:13.3px;color:var(--ink);width:330px;margin:0 auto}
  .why__cta{font-size:15.5px;font-weight:700;color:var(--orange);margin:9px 0 10px}
  .why__note{font-size:8.8px;line-height:13.3px;color:var(--ink);width:330px;margin:0 auto 13px}
  .why__note a{color:var(--orange)}
  .care-photo{left:91px;top:207px;width:288px;height:288px;border-radius:50%;background:linear-gradient(150deg,#f4efe9,#e3ded8 45%,#c5ccd6 70%,#8fa3b8 90%);box-shadow:0 0 0 5px var(--white),0 3px 8px rgba(0,0,0,.25)}
  .contact{top:514px;width:110px;text-align:center}
  .contact__icon{width:40px;height:40px;border-radius:50%;background:var(--orange);margin:0 auto 10px;display:flex;align-items:center;justify-content:center}
  .contact__label{font-size:9.5px;font-weight:500;color:var(--ink)}
  .contact__value{font-size:7.8px;color:var(--ink);margin-top:3px}
  .contact--address{left:55px}
  .contact--email{left:188px}
  .contact--phone{left:305px}
  .contact-divider{top:514px;width:1px;height:80px;background:#d5d5d5}
</style>
</head>
<body>

<section class="page page--front">
  <svg class="page__shapes" width="471" height="665" viewBox="0 0 471 665">
    <circle cx="356" cy="76" r="141" fill="none" stroke="var(--orange)" stroke-width="30"/>
    <circle cx="235" cy="286" r="148" fill="var(--white)"/>
    <circle cx="235" cy="286" r="144" fill="var(--grey)"/>
    <circle cx="235" cy="286" r="131" fill="none" stroke="var(--grey-ring)" stroke-width="3"/>
    <circle cx="235" cy="286" r="118" fill="none" stroke="var(--grey-ring)" stroke-width="2"/>
    <circle cx="23" cy="467" r="24" fill="var(--grey-soft)"/>
    <circle cx="259" cy="467" r="24" fill="var(--grey-soft)"/>
    <path d="M0 665 C60 630 140 612 210 614 C290 616 340 640 400 636 C440 633 460 625 471 617 L471 665 Z" fill="var(--orange)"/>
  </svg>

  <div class="abs brand"><span class="brand__dot"></span>Clearview MRI</div>
  <div class="abs scanner-photo" role="img" aria-label="Photo of an MRI scanner with patient table"></div>
  <div class="abs exam-photo" role="img" aria-label="Photo of a radiologist preparing a patient on the scanner table"></div>

  <div class="abs intro">
    <h2 class="intro__title">INTRODUCTION</h2>
    <p class="intro__text">Hello and thank you for your interest in our Clearview MRI imaging services. At Clearview MRI, we specialize in advanced MRI screenings that can provide valuable insights into your heart health and overall whole-body well-being. Today, I'd like to share some information about our cardiac MRI screening and whole-body MRI screening services."</p>
  </div>

  <div class="abs service service--cardiac">
    <h3 class="service__title">Cardiac MRI Screening</h3>
    <p class="service__text">This non-invasive procedure allows us to capture detailed images of your heart's structure and its function. It helps in diagnosing various heart conditions, including coronary artery disease, heart valve issues, and myocardial diseases.</p>
    <p class="service__price">$3000 -$2500</p>
  </div>

  <div class="abs service service--body">
    <h3 class="service__title">Whole-Body MRI Screening</h3>
    <p class="service__text">In addition to cardiac MRI, we offer comprehensive whole-body MRI screening. Includes Head, Neck, Cervical Spine, Thoracic Spine, Lumbar Spine, and Pelvis. This advanced imaging technique covers various organs and tissues, providing a holistic view of your health.</p>
    <p class="service__price">$2500- $2000</p>
  </div>
</section>

<section class="page page--back">
  <svg class="page__shapes" width="471" height="665" viewBox="0 0 471 665">
    <circle cx="235" cy="60" r="292" fill="var(--grey)"/>
    <circle cx="235" cy="60" r="262" fill="var(--orange)"/>
    <circle cx="235" cy="60" r="222" fill="var(--white)"/>
    <path d="M0 665 C60 630 140 612 210 614 C290 616 340 640 400 636 C440 633 460 625 471 617 L471 665 Z" fill="var(--orange)"/>
  </svg>

  <div class="abs why">
    <h2 class="why__title">Why Choose Us?</h2>
    <p class="why__lead">Our expert team is dedicated to your well-being, providing top-notch imaging services with state-of-the-art technology.</p>
    <h3 class="why__cta">Call Now to Book Your Appointment!</h3>
    <p class="why__note">Don't miss out on this incredible offer! Contact us at <a href="tel:5550142276">555 014 2276</a> to schedule your MRI screening and secure your $500 discount. Limited slots available!</p>
    <p class="why__note">Thank you for considering Clearview MRI. We look forward to serving you and assisting you in maintaining your health through advanced MRI imaging.</p>
  </div>

  <div class="abs care-photo" role="img" aria-label="Photo of a doctor guiding a patient into an MRI scanner"></div>

  <div class="abs contact contact--address">
    <div class="contact__icon">
      <svg width="14" height="16" viewBox="0 0 14 16"><path d="M7 1a5 5 0 0 0-5 5c0 3.5 5 9 5 9s5-5.5 5-9a5 5 0 0 0-5-5z" fill="var(--white)"/><circle cx="7" cy="6" r="1.8" fill="var(--orange)"/></svg>
    </div>
    <p class="contact__label">Address :</p>
    <p class="contact__value">123,Lorem ipsum dolor sit</p>
  </div>
  <div class="abs contact-divider" style="left:173px"></div>
  <div class="abs contact contact--email">
    <div class="contact__icon">
      <svg width="16" height="12" viewBox="0 0 16 12"><rect x="1" y="1" width="14" height="10" rx="1.5" fill="var(--white)"/><path d="M1.5 2 L8 7 L14.5 2" fill="none" stroke="var(--orange)" stroke-width="1.3"/></svg>
    </div>
    <p class="contact__label">Email Address :</p>
    <p class="contact__value">info@companyname.com</p>
  </div>
  <div class="abs contact-divider" style="left:310px"></div>
  <div class="abs contact contact--phone">
    <div class="contact__icon">
      <svg width="14" height="14" viewBox="0 0 24 24"><path d="M6.6 10.8a15 15 0 0 0 6.6 6.6l2.2-2.2a1 1 0 0 1 1-.25 11.4 11.4 0 0 0 3.6.57 1 1 0 0 1 1 1V20a1 1 0 0 1-1 1A17 17 0 0 1 3 4a1 1 0 0 1 1-1h3.5a1 1 0 0 1 1 1c0 1.250.2 2.450.57 3.57a1 1 0 0 1-.25 1z" fill="var(--white)"/></svg>
    </div>
    <p class="contact__label">Phone :</p>
    <p class="contact__value">+1 888 888 8888</p>
  </div>
</section>

</body>
</html>
```